Health and Wellness company needs flyer to promote free seminar

Stride reform studio is a health and wellness company that offers an exercise program designed by physical therapists to help relieve pain and improve mobility. Our business is a new concept that is not well understood by the public. In order to promote our business we offer a free seminar where we present information regarding the underlying cause of pain and tightness. During the seminar we also perform a posture screen and movement testing for all participants.

Target Market(s)

Mostly healthy and active women ages 25-65

Industry/Entity Type

Health And Wellness

Font styles to use
Sans Serif

Colors

Designer to choose colors to be used in the design.

Requirements
Must have
• Title: Eliminate Pain and Tightness For Good
• Paragraph: Stride Reform Studio offers a free 60 minute seminar: "The Busy Walker's Handbook to Bending and Standing Taller."
• What to Expect:
• • Identify the underlying cause of your pain and mobility issues
• • Expose what gets in the way of you moving and feeling better
• • Learn why traditional exercises don’t help and can actually make the problem worse
• • Reveal what your posture is saying and how that impacts you
• • Experience your muscle imbalances through movement tests
• • Discover the training method that realigns your posture, increases your mobility and reduces your pain
• Call to action: RSVP online at stridereformstudio.com
Nice to have
• Use a relevant image showing a female dealing with tightness in the low back, legs, etc.
• Emphasize that the seminar is FREE.
• Make the call to action prominent.

```html
<!DOCTYPE html>
<html lang="en">
<head>
<meta charset="utf-8">
<title>Stride Reform Studio – Free Seminar</title>
<link rel="stylesheet" href="https://fonts.googleapis.com/css2?family=Lato:wght@300;400;700&family=Open+Sans:wght@400;600;700&display=swap">
<style>
  :root {
    --orange: #f7931e;
    --orange-light: #f9a33a;
    --indigo: #4a4fb0;
    --indigo-deep: #3d3ea8;
    --grey-band: #e6e6e6;
    --ink: #3a3a3a;
    --body: #4d4d4d;
    --white: #ffffff;
  }
  * { box-sizing: border-box; margin: 0; padding: 0; }
  html, body { width: 848px; height: 1200px; overflow: hidden; background: var(--white); }
  .flyer { position: relative; width: 848px; height: 1200px; overflow: hidden; background: var(--white); font-family: "Open Sans", sans-serif; }

  .hero { position: absolute; left: 0; top: 0; width: 848px; height: 552px; }
  .hero svg { position: absolute; left: 0; top: 0; }

  .hero-photo {
    position: absolute; left: 0; top: 0; width: 420px; height: 552px;
    background: linear-gradient(160deg, #d9a184 0%, #e6cfc2 40%, #d2d2d2 70%, #c4c4c4 100%);
  }

  .headline { position: absolute; left: 0; top: 0; font-family: "Lato", sans-serif; color: var(--white); font-weight: 700; text-transform: uppercase; }
  .headline span { position: absolute; white-space: nowrap; line-height: 1; }
  .headline .l1 { left: 426px; top: 176px; font-size: 34px; }
  .headline .l2 { left: 495px; top: 228px; font-size: 34px; }
  .headline .l3 { left: 558px; top: 280px; font-size: 46.5px; }

  .hero-rule { position: absolute; left: 498px; top: 366px; width: 302px; height: 1px; background: var(--white); }

  .hero-intro { position: absolute; left: 511px; top: 396px; width: 290px; font-family: "Lato", sans-serif; font-weight: 300; font-size: 15.5px; line-height: 26.4px; color: var(--white); text-transform: uppercase; }
  .hero-intro strong { font-weight: 700; }

  .invite { position: absolute; left: 0; top: 0; }
  .invite-band { position: absolute; display: flex; align-items: center; justify-content: center; font-family: "Open Sans", sans-serif; font-weight: 700; text-transform: uppercase; }
  .band-top { left: 32px; top: 684px; width: 296px; height: 48px; background: var(--orange); color: var(--white); font-size: 28px; clip-path: polygon(5% 0, 100% 0, 95% 100%, 0 100%); }
  .band-mid { left: 80px; top: 737px; width: 230px; height: 45px; background: var(--grey-band); color: var(--ink); font-size: 19px; clip-path: polygon(0 0, 92% 0, 100% 100%, 8% 100%); }
  .band-bottom { left: 52px; top: 785px; width: 296px; height: 49px; background: var(--indigo); color: var(--white); font-size: 30px; clip-path: polygon(6% 0, 100% 0, 94% 100%, 0 100%); }

  .cta-lead { position: absolute; left: 54px; top: 876px; font-size: 34px; font-weight: 600; color: var(--ink); white-space: nowrap; }
  .cta-url { position: absolute; left: 95px; top: 934px; font-size: 21px; font-weight: 700; color: var(--ink); white-space: nowrap; }

  .brand { position: absolute; left: 38px; top: 1024px; display: flex; align-items: center; gap: 12px; }
  .brand-mark { width: 60px; height: 60px; background: var(--orange); }
  .brand-name { font-family: "Open Sans", sans-serif; font-weight: 700; font-size: 26px; color: var(--indigo); white-space: nowrap; letter-spacing: -0.3px; }

  .expect { position: absolute; left: 408px; top: 616px; width: 398px; }
  .expect-title { font-size: 23px; font-weight: 700; color: var(--orange); text-transform: uppercase; margin-bottom: 28px; }
  .expect-list { list-style: none; }
  .expect-list li { font-size: 16.5px; line-height: 25px; color: var(--body); height: 77px; text-align: left; }
  .expect-list li.justified { text-align: justify; }
  .expect-list li strong { color: var(--indigo); font-weight: 600; }
</style>
</head>
<body>
<main class="flyer">
  <section class="hero">
    <svg width="848" height="552" viewBox="0 0 848 552" aria-hidden="true">
      <polygon points="0,0 140,0 0,60" fill="var(--orange)"/>
      <polygon points="560,0 848,0 848,70 600,110" fill="var(--orange-light)"/>
      <polygon points="460,40 720,0 760,120 440,150" fill="var(--orange)"/>
      <polygon points="620,0 848,0 848,40" fill="#fbd1a0"/>
      <polygon points="360,150 848,55 848,552 400,552" fill="var(--indigo-deep)"/>
      <polygon points="700,90 848,55 848,300" fill="var(--indigo)"/>
      <polygon points="400,552 560,400 848,552" fill="#4347ad"/>
    </svg>
    <div class="hero-photo" role="img" aria-label="Photo of a woman seen from behind, holding her sore shoulder"></div>
    <h1 class="headline">
      <span class="l1">Eliminate Pain</span>
      <span class="l2">and Tightness</span>
      <span class="l3">For Good</span>
    </h1>
    <div class="hero-rule"></div>
    <p class="hero-intro">Stride Reform Studio offers a <strong>free 60 minute seminar</strong>: "The Busy Walker's Handbook to Bending and Standing Taller."</p>
  </section>

  <div class="invite">
    <div class="invite-band band-top">We invite you</div>
    <div class="invite-band band-mid">to attend a</div>
    <div class="invite-band band-bottom">Free seminar</div>
  </div>

  <p class="cta-lead">Sign up online at</p>
  <p class="cta-url">stridereformstudio.com</p>

  <div class="brand">
    <div class="brand-mark"></div>
    <span class="brand-name">stride reform studio</span>
  </div>

  <section class="expect">
    <h2 class="expect-title">What to expect</h2>
    <ul class="expect-list">
      <li><strong>Identify</strong> the underlying cause of your pain and mobility issues.</li>
      <li><strong>Expose</strong> what gets in the way of you moving and feeling better.</li>
      <li><strong>Learn</strong> why traditional exercises don’t help and can actually make the problem worse.</li>
      <li><strong>Reveal</strong> what your posture is saying and how that impacts you.</li>
      <li><strong>Experience</strong> your muscle imbalances through movement tests.</li>
      <li class="justified"><strong>Discover</strong> the training method that realigns your posture, increases your mobility and reduces your pain.</li>
    </ul>
  </section>
</main>
</body>
</html>
```